Linden Medical - Flyer

We are a full service pharmacy that specializes in diabetic testing and medications. We research the patient's insurance to maximize their insurance benefit and then deliver the medications monthly directly to the patient's doorstep, for free! We save the patient, time and money every month.
We would love a flyer that we can distribute to Doctor's offices and patients that sum up our pharmacy. Emphasis on saving money, time, and getting the best quality supplies by maximizing their insurance. We want it to be eye catching, clean, and professional.
You can use our logo or feel free to make your own design.
Updates
Target Market(s)
diabetic patients wanting to save money
Industry/Entity Type
Insurance
Look and feel
Each slider illustrates characteristics of the customer's brand and the style your logo design should communicate.

```html
<!DOCTYPE html>
<html lang="en">
<head>
<meta charset="utf-8">
<title>Linden Medical – Flyer</title>
<link href="https://fonts.googleapis.com/css2?family=Arimo:wght@400;700&display=swap" rel="stylesheet">
<style>
  :root {
    --bg-left: #e6f3ef;
    --bg-mid: #bfe8d9;
    --bg-right: #55d4a4;
    --teal-ink: #2f7375;
    --grey-ink: #6d7e80;
    --copy-ink: #3a7d80;
    --mark-green: #8fcf3c;
    --scrub-blue: #3e97dc;
    --scrub-light: #7fc0ee;
    --scrub-deep: #2c7fc4;
  }
  * { margin: 0; padding: 0; box-sizing: border-box; }
  html, body { width: 1200px; height: 1000px; overflow: hidden; }
  body { font-family: "Arimo", Arial, sans-serif; }

  .flyer {
    position: relative;
    width: 1200px;
    height: 1000px;
    background: linear-gradient(90deg, var(--bg-left) 0%, var(--bg-mid) 45%, var(--bg-right) 100%);
    overflow: hidden;
  }

  .brand { position: absolute; left: 30px; top: 86px; display: flex; align-items: center; }
  .brand-square {
    width: 196px; height: 196px;
    background: var(--mark-green);
    margin-right: 40px;
    margin-top: 20px;
  }
  .brand-name { font-weight: 400; line-height: 1; }
  .brand-name .line-1 {
    display: block; font-size: 76px; letter-spacing: 6px; color: var(--teal-ink);
  }
  .brand-name .line-2 {
    display: block; font-size: 50px; letter-spacing: 7px; margin-top: 30px; margin-left: 4px;
    color: var(--grey-ink);
  }

  .photo-clinician {
    position: absolute; left: 856px; top: 0; width: 344px; height: 422px;
    background:
      radial-gradient(ellipse 90px 60px at 150px 200px, rgba(240,242,245,0.9), rgba(240,242,245,0) 100%),
      radial-gradient(ellipse 70px 50px at 160px 260px, rgba(232,190,170,0.85), rgba(232,190,170,0) 100%),
      linear-gradient(160deg, var(--scrub-light) 0%, var(--scrub-blue) 55%, var(--scrub-deep) 100%);
  }

  .photo-strip { position: absolute; left: 0; top: 422px; width: 1200px; height: 202px; display: flex; }
  .strip-panel { height: 100%; }
  .panel-search {
    width: 282px;
    background:
      radial-gradient(ellipse 90px 80px at 140px 100px, #f2a51c 0%, #f6c45a 45%, rgba(250,250,248,0) 100%),
      #fbfbfa;
  }
  .panel-keyboard {
    width: 284px;
    background:
      radial-gradient(ellipse 80px 65px at 158px 92px, #2f7fd6 0%, #2566b8 60%, rgba(40,44,50,0) 100%),
      linear-gradient(135deg, #3b3e44, #1f2226);
  }
  .panel-testing {
    width: 284px;
    background:
      radial-gradient(ellipse 90px 70px at 120px 120px, #e8c4b2 0%, rgba(232,196,178,0) 100%),
      radial-gradient(ellipse 70px 60px at 200px 150px, #dcb5a3 0%, rgba(220,181,163,0) 100%),
      linear-gradient(135deg, #f3f6f8, #d9e6ee);
  }
  .panel-tablets {
    width: 350px;
    background:
      radial-gradient(ellipse 80px 50px at 110px 110px, #8ec2e6 0%, rgba(142,194,230,0) 100%),
      radial-gradient(ellipse 80px 40px at 170px 170px, #d8616a 0%, rgba(216,97,106,0) 100%),
      radial-gradient(ellipse 70px 60px at 280px 70px, #3f7560 0%, rgba(63,117,96,0) 100%),
      radial-gradient(ellipse 90px 50px at 90px 40px, #e9d3c6 0%, rgba(233,211,198,0) 100%),
      linear-gradient(135deg, #e4ecef, #cfdfe8);
  }

  .benefits {
    position: absolute; left: 90px; top: 720px;
    list-style: none;
    color: var(--copy-ink);
    font-weight: 700;
    font-size: 28px;
    line-height: 36px;
    letter-spacing: 1px;
  }
  .promise {
    position: absolute; left: 816px; top: 720px; width: 380px;
    text-align: center;
    color: var(--copy-ink);
    font-weight: 700;
    font-size: 28px;
    line-height: 36px;
    letter-spacing: 1px;
  }
</style>
</head>
<body>
<main class="flyer">
  <header class="brand">
    <div class="brand-square"></div>
    <h1 class="brand-name"><span class="line-1">LINDEN</span><span class="line-2">MEDICAL</span></h1>
  </header>

  <div class="photo-clinician" role="img" aria-label="Clinician in blue scrubs with stethoscope writing on a clipboard"></div>

  <section class="photo-strip">
    <div class="strip-panel panel-search" role="img" aria-label="Figure searching with a magnifying glass"></div>
    <div class="strip-panel panel-keyboard" role="img" aria-label="Keyboard with a blue Save Money key"></div>
    <div class="strip-panel panel-testing" role="img" aria-label="Finger-prick blood glucose test"></div>
    <div class="strip-panel panel-tablets" role="img" aria-label="Colourful tablets in blister packs"></div>
  </section>

  <ul class="benefits">
    <li>...full service pharmacy</li>
    <li>....saving money</li>
    <li>.....saving time</li>
    <li>......best quality supplies</li>
  </ul>

  <p class="promise">We save the patient,<br>time and money.</p>
</main>
</body>
</html>
```